Design an authentic and very luxury business card for a company

Design an authentic and very luxury standart size business card 90x50 mm

On the first side of the business card we need only logo of our company group with nice backround. Logo of company group is the first attached file called "gold". The name of coumpany group is "Vertical harbor group".

On the other side of business card should be given information which you will find in the second file and the logo of the company VHG SKYR. Logo is attached too (third file)

We prefer having both sides of the business card in different colours to make them look more unique and the edge of business card can have its own colour too. Business card could also have patterns and/or indentations (like the last attached file as an example).The way how you design the information about partilucar contact person, websites and adresses - is completely up to you. We need authentic and luxury looking business card. If need you more information or you need logos in other formats I will provide everything gladly.

Last two files I attached only as an examples to show what looks quite well from our point of view. What concerns manufacturing of business cards - we are completely open so if you see that your proposed design will look exceptionally well with particular production type - we are open for your ideas.

If you need further information feel free to contact us.

Best regards

```html
<!DOCTYPE html>
<html lang="en">
<head>
<meta charset="utf-8">
<title>Vertical Harbor Group – Business Card</title>
<link href="https://fonts.googleapis.com/css2?family=Montserrat:wght@500;600;700&family=Open+Sans:wght@400;600&display=swap" rel="stylesheet">
<style>
  :root {
    --stage-dark: #1c1d20;
    --stage-light: #5a5c61;
    --card-black: #0d0d0e;
    --card-black-soft: #232326;
    --gold: #d6a21e;
    --card-white: #ffffff;
    --brand-blue: #1a78c8;
    --ink: #222326;
    --ink-soft: #55575c;
  }
  * { box-sizing: border-box; margin: 0; padding: 0; }
  html, body { width: 1200px; height: 900px; overflow: hidden; }
  body {
    background: radial-gradient(ellipse at 40% 30%, var(--stage-light) 0%, var(--stage-dark) 75%);
    position: relative;
    font-family: "Open Sans", Arial, sans-serif;
  }
  .card {
    position: absolute;
    width: 520px;
    height: 289px;
    border-radius: 22px;
    overflow: hidden;
    box-shadow: 0 18px 40px rgba(0,0,0,.45);
  }
  /* Front side */
  .card--front {
    left: 90px; top: 170px;
    background: var(--card-black);
  }
  .front-texture {
    position: absolute; inset: 0;
    background: radial-gradient(ellipse at 50% 40%, var(--card-black-soft) 0%, var(--card-black) 80%);
  }
  .front-brand {
    position: absolute; left: 0; right: 0; top: 0; bottom: 0;
    display: flex; align-items: center; justify-content: center; gap: 14px;
  }
  .front-brand__mark {
    width: 22px; height: 22px; background: var(--gold);
  }
  .front-brand__name {
    font-family: "Montserrat", Arial, sans-serif;
    font-weight: 700;
    font-size: 27px;
    letter-spacing: 1px;
    color: var(--gold);
    text-transform: uppercase;
  }
  /* Back side */
  .card--back {
    left: 590px; top: 440px;
    background: var(--card-white);
  }
  .back-edge {
    position: absolute; right: 0; top: 72px;
    width: 10px; height: 26px; background: var(--brand-blue);
  }
  .back-brand {
    position: absolute; left: 40px; top: 38px;
    display: flex; align-items: center; gap: 14px;
  }
  .back-brand__mark {
    width: 18px; height: 18px; border-radius: 50%; background: var(--brand-blue);
  }
  .back-brand__name {
    font-family: "Montserrat", Arial, sans-serif;
    font-weight: 700;
    font-size: 48px;
    letter-spacing: 1px;
    color: var(--brand-blue);
  }
  .person {
    position: absolute; right: 30px; top: 118px; text-align: right;
  }
  .person__name {
    font-weight: 600; font-size: 17px; color: var(--brand-blue);
  }
  .person__title {
    font-size: 10px; color: var(--ink-soft); margin-top: 1px;
  }
  .person__address {
    font-size: 11.5px; color: var(--ink); margin-top: 10px; line-height: 1.45;
  }
  .contacts {
    position: absolute; left: 26px; bottom: 26px;
    list-style: none;
  }
  .contacts li {
    display: flex; align-items: center; gap: 8px;
    font-size: 11.5px; color: var(--ink); line-height: 1.65;
  }
  .contacts svg { width: 11px; height: 11px; flex: none; }
</style>
</head>
<body>

<section class="card card--front" aria-label="Front side">
  <div class="front-texture" role="img" aria-label="Black card surface with embossed scale pattern"></div>
  <div class="front-brand">
    <span class="front-brand__mark"></span>
    <span class="front-brand__name">Vertical Harbor Group</span>
  </div>
</section>

<section class="card card--back" aria-label="Back side">
  <span class="back-edge"></span>
  <div class="back-brand">
    <span class="back-brand__mark"></span>
    <span class="back-brand__name">VHG SKYR</span>
  </div>

  <div class="person">
    <p class="person__name">Daniel Marsh</p>
    <p class="person__title">Funder &amp; CEO</p>
    <p class="person__address">Location Or Address<br>1820 n.14 th st dalton,TX 75219</p>
  </div>

  <ul class="contacts">
    <li>
      <svg viewBox="0 0 12 12"><circle cx="6" cy="6" r="6" fill="var(--brand-blue)"/><path d="M4 3.2l1 1.4-.6.7a4 4 0 0 0 2.3 2.3l.7-.6 1.4 1-.6 1A5.4 5.4 0 0 1 3 4z" fill="#fff"/></svg>
      000 3870 2214
    </li>
    <li>
      <svg viewBox="0 0 12 12"><circle cx="6" cy="6" r="6" fill="var(--brand-blue)"/><rect x="3" y="4" width="6" height="4" fill="#fff"/><path d="M3 4l3 2.2L9 4" stroke="var(--brand-blue)" stroke-width=".7" fill="none"/></svg>
      info@vhgskyr.com
    </li>
    <li>
      <svg viewBox="0 0 12 12"><circle cx="6" cy="6" r="6" fill="var(--brand-blue)"/><circle cx="6" cy="6" r="3" fill="none" stroke="#fff" stroke-width=".8"/><path d="M3 6h6M6 3v6" stroke="#fff" stroke-width=".6"/></svg>
      www.vhgskyr.com
    </li>
  </ul>
</section>

</body>
</html>
```